Bail Bond post card mailer.

CourtKeyNexus.com sells

1. Direct guaranteed leads to bail bond agents
2. Website creation
3. Website SEO / MOBILE review
4. Back Links from our network of bailbond / jail websites

Our target customer is a bail bond company either big or small...

Our MAIN GOAL is to get more customers that want LEADS, yet we do offer the services.

We're wanting to do a post card mailer, that depicts the ever changing landscape of marketing. For instance phone books are not very relevant anymore, nor are phone booths etc. Times are changing and it requires changes how to attract customers online.

We're wanting the "call to action" on the post card to be directing the user to a specific URL, where they will enter their promotional code. ( We're not sure if the promotional code will be a sticker or on the address label ) We're open to thoughts on this:

We'll want to also have an email address and a phone number for bail bond agents to contact us.

Feel Free to visit courtkeynexus.com to take a look at the core website

```html
<!DOCTYPE html>
<html lang="en">
<head>
<meta charset="utf-8">
<title>Court Key Nexus — Postcard Mailer</title>
<link href="https://fonts.googleapis.com/css2?family=Poppins:wght@300;400;700&display=swap" rel="stylesheet">
<style>
  :root {
    --page: #ffffff;
    --brand-blue: #0d4580;
    --guide-line: rgba(255, 255, 255, 0.28);
    --text-light: #ffffff;
    --text-soft: rgba(255, 255, 255, 0.85);
    --interior-top: #7f9cc4;
    --interior-bottom: #c4a27a;
    --sky: #9ec1ea;
    --yard: #9d9c97;
    --cellblock-light: #dcdcd8;
    --cellblock-dark: #8f8d88;
  }
  html, body {
    margin: 0;
    padding: 0;
    width: 1200px;
    height: 986px;
    overflow: hidden;
    background: var(--page);
  }
  .postcard {
    position: absolute;
    left: 17px;
    top: 39px;
    width: 1147px;
    height: 887px;
    box-shadow: 0 6px 18px rgba(0, 0, 0, 0.35);
    overflow: hidden;
    font-family: "Poppins", sans-serif;
    color: var(--text-light);
  }
  .brand-panel {
    position: absolute;
    left: 0;
    top: 0;
    width: 790px;
    height: 887px;
    box-sizing: border-box;
    padding: 92px 60px 0 154px;
    background: var(--brand-blue);
    display: flex;
    flex-direction: column;
    overflow: hidden;
  }
  .guide-lines {
    position: absolute;
    inset: 0;
    width: 100%;
    height: 100%;
  }
  .brand-panel > *:not(.guide-lines) { position: relative; }
  .wordmark {
    margin: 0;
    font-size: 132px;
    line-height: 0.98;
    letter-spacing: -3px;
    white-space: nowrap;
  }
  .wordmark span { display: block; }
  .wordmark__bold { font-weight: 700; }
  .wordmark__light { font-weight: 300; }
  .services {
    list-style: none;
    margin: 30px 0 0;
    padding: 0;
    font-size: 20px;
    font-weight: 300;
    line-height: 1.5;
    color: var(--text-soft);
  }
  .services li::before {
    content: "";
    display: inline-block;
    width: 8px;
    height: 8px;
    margin: 0 14px 3px 0;
    background: var(--text-light);
  }
  .call-to-action {
    margin: 30px 0 0;
    font-size: 20px;
    font-weight: 400;
    line-height: 1.3;
  }
  .web-address {
    display: block;
    font-size: 25px;
    font-weight: 700;
  }
  .contact {
    margin: 14px 0 0;
    font-size: 18px;
    font-weight: 300;
    color: var(--text-soft);
  }
  .contact strong { font-weight: 700; color: var(--text-light); }
  .photo-column {
    position: absolute;
    left: 793px;
    top: 0;
    width: 354px;
    height: 887px;
    display: flex;
    flex-direction: column;
    gap: 3px;
  }
  .photo { width: 100%; }
  .photo--dayroom {
    height: 273px;
    background: linear-gradient(180deg, var(--interior-top), var(--interior-bottom));
  }
  .photo--facility {
    height: 270px;
    background: linear-gradient(180deg, var(--sky) 0%, var(--sky) 40%, var(--yard) 100%);
  }
  .photo--cellblock {
    flex: 1;
    background: linear-gradient(180deg, var(--cellblock-light), var(--cellblock-dark));
  }
</style>
</head>
<body>
  <main class="postcard">
    <section class="brand-panel">
      <svg class="guide-lines" viewBox="0 0 790 887" preserveAspectRatio="none" aria-hidden="true">
        <line x1="0" y1="0" x2="790" y2="887" stroke="var(--guide-line)" stroke-width="1.5" stroke-dasharray="10 8"/>
        <line x1="790" y1="300" x2="0" y2="887" stroke="var(--guide-line)" stroke-width="1.5" stroke-dasharray="10 8"/>
      </svg>
      <h1 class="wordmark">
        <span class="wordmark__bold">Court</span>
        <span class="wordmark__bold">Key</span>
        <span class="wordmark__light">Nexus</span>
      </h1>
      <ul class="services">
        <li>Direct guaranteed leads for bail bond agents</li>
        <li>Website creation</li>
        <li>Website SEO &amp; mobile review</li>
        <li>Back links from our bail bond &amp; jail site network</li>
      </ul>
      <p class="call-to-action">Enter the promo code on your label at
        <span class="web-address">http://www.courtkeynexus.com/</span>
      </p>
      <p class="contact"><strong>(555) 014-2287</strong> &nbsp;·&nbsp; leads@courtkeynexus.com</p>
    </section>
    <aside class="photo-column">
      <div class="photo photo--dayroom" role="img" aria-label="Photo of a jail dayroom with inmates seated facing a television"></div>
      <div class="photo photo--facility" role="img" aria-label="Photo of a correctional facility entrance behind a fence with flags"></div>
      <div class="photo photo--cellblock" role="img" aria-label="Photo of a two-tier cell block with barred doors"></div>
    </aside>
  </main>
</body>
</html>
```